Business Card and Letterhead for Juniper Anvil - (Have Logo)

Update 4: Removed company reg no from business card details as it looked a bit out of place. Updated services list.
UPDATE 3
Sorry, I got the address a little bit wrong, have updated it below. Sorry for any inconvenience caused.
UPDATE 2
Finally I have the details for the business cards and letterhead. Submissions already made do not have to be updated unless shortlisted, if all new submissions could include the details for me, Marcus, that would be very much appreciated and help with the final shortlist selection. I intend to share a shortlist of the three best entries with past and existing customers for their feedback and opinions. Thank you all again for your time.
Here are the details.
Marcus Telby
Web Developer
T: 01632 960 418
E: marcus@juniperanvil.example
www.juniperanvil.example
Professional Photography
Web Solutions & E-Commerce
Audio & HD Video Production
Marketing & Promotions
Identity and Branding
Juniper Anvil Ltd
Suite 20938, 3rd Floor
212-224 Orchard Lane
London, N7 9QX
Company Reg. No: 05829147
The order and the layout of the information are of course down to the design, but the company registration number should be smaller and less prominent. The formatting of the telephone and email address using a T: and an E: I am not sure about and again if it is Tel: or Email: or Icons is up to the design.
The Company No. on the letterhead should read (somewhere in small text along the bottom):
Juniper Anvil is a Ltd Company registered in England & Wales, Registration No. 05829147.
The second business card details are
Oliver Brackley
Photographer
T: 01632 960 418
E: oliver@juniperanvil.example
Everything else the same of course.
Thank you again for all the submissions so far.
END OF UPDATE 2
-
UPDATE 1: Please do not alter the logo nor the logo colours. (This was a previous pixel forum project and I am extremely happy with it. The icon can stand alone of course, but I have had to eliminate all entries that have made it black and white, or reversed the icon.) I would like to thank everyone that has participated so far and am very grateful for all your thought and time.
End of Update 1
-
Original Brief:
I have attached the logo vector file.
Following a superb logo from a previous Pixel Forum project I am now looking for a business card design and (although less important) a letterhead as well.
I must admit I tried to do it myself but could only come up with the usual amateur stuff that in comparison to the quality of the logo looked awful.
About Us
Juniper Anvil Ltd will be a new company due to start in January. It is really just me (a web developer) and my friend (a photographer). We will be aiming at the usual small to medium sized businesses in the local area, selling various digital services including photographic services to the public, web hosting and development, commercial photography, modelling services (not us!), full video and film production and possibly a bit of marketing as well. (Really it is anything we can do professionally all lumped together! We met running seperate businesses which have both since closed)
We will not be competing on price. We plan to be expensive but fair. Certainly not the cheapest.
What we are looking for
Business Card
I imagine a double sided business card, which will be used for more than one person. I imagine the front to be the same for everyone and the persons details to be on the back, although this is of course only my thoughts and I am of course completely open to any ideas.
The card could also have a services list or a bit about what we do on it. It might feature the website address, our business address (mail forwarding address) or our registered company number.
Or it might have none of that, we are completely open to any ideas and have no real fixed opinions. I just want it to be really nice :-)
Letterhead (secondary importance)
We will make our decision primarily on the business card, although a mathcing letterhead would be fantastic. Something standardish in format and simple, although again, all ideas are welcomed.
I hope that is enough information but if you have any questions I will answer them as fully and as quickly as possible.
Thank you once again and I really look forward to seeing your ideas and picking a winner.
Marcus T.
Small businesses AND the general public
Film Production

```html
<!DOCTYPE html>
<html lang="en">
<head>
<meta charset="utf-8">
<title>Juniper Anvil – Stationery</title>
<link rel="stylesheet" href="https://fonts.googleapis.com/css2?family=Open+Sans:wght@400;600;800&display=swap">
<style>
  :root {
    --stage: #000000;
    --paper: #ffffff;
    --card-front: #f3f3f3;
    --brand-red: #b3121c;
    --ink: #3a3a3a;
    --muted: #6a6a6a;
    --blush: #f6e5de;
    --fog: #ebebeb;
  }
  * { margin: 0; padding: 0; box-sizing: border-box; }
  html, body { width: 1200px; height: 1114px; overflow: hidden; }
  body {
    background: var(--stage);
    position: relative;
    font-family: "Open Sans", Arial, sans-serif;
    color: var(--ink);
  }
  .wordmark {
    position: absolute;
    display: flex;
    align-items: center;
    gap: 8px;
    font-weight: 800;
    color: var(--brand-red);
    text-transform: uppercase;
    letter-spacing: 0.5px;
    white-space: nowrap;
    line-height: 1;
  }
  .wordmark .mark-square { display: block; background: var(--brand-red); flex: none; }

  /* Letterhead */
  .letterhead {
    position: absolute;
    left: 96px; top: 60px;
    width: 730px; height: 1032px;
    background: var(--paper);
    overflow: hidden;
  }
  .letterhead .wordmark { left: 44px; top: 50px; font-size: 26px; }
  .letterhead .wordmark .mark-square { width: 26px; height: 26px; }
  .letterhead .blush-block {
    position: absolute; left: 0; top: 552px;
    width: 318px; height: 356px; background: var(--blush);
  }
  .letterhead .fog-block {
    position: absolute; left: 0; top: 908px;
    width: 318px; height: 86px; background: var(--fog);
  }
  .letterhead .footer-band {
    position: absolute; left: 0; bottom: 0;
    width: 100%; height: 38px;
    background: var(--brand-red);
    display: flex; align-items: center; justify-content: center;
  }
  .registration {
    color: var(--paper);
    font-size: 9px;
    letter-spacing: 0.2px;
  }

  /* Business cards */
  .card { position: absolute; border-radius: 10px; overflow: hidden; }
  .card-front {
    left: 856px; top: 62px;
    width: 310px; height: 180px;
    background: var(--card-front);
  }
  .card-front .blush-block {
    position: absolute; left: 0; top: 8px;
    width: 98px; height: 130px; background: var(--blush);
  }
  .card-front .wordmark { right: 14px; bottom: 30px; font-size: 15px; gap: 5px; }
  .card-front .wordmark .mark-square { width: 15px; height: 15px; }

  .card-back {
    left: 848px; top: 264px;
    width: 312px; height: 180px;
    background: var(--paper);
  }
  .card-back .wordmark { left: 12px; top: 24px; font-size: 15px; gap: 5px; }
  .card-back .wordmark .mark-square { width: 15px; height: 15px; }
  .card-back .blush-block {
    position: absolute; right: 4px; top: 10px;
    width: 122px; height: 136px; background: var(--blush);
  }
  .card-back .fog-block {
    position: absolute; right: 4px; top: 146px;
    width: 122px; height: 32px; background: var(--fog);
  }
  .contact {
    position: absolute;
    left: 12px; top: 68px;
    width: 170px;
  }
  .contact .name { font-size: 10px; line-height: 13px; color: var(--ink); font-weight: 600; }
  .contact .role { font-size: 9px; line-height: 12px; color: var(--brand-red); margin-bottom: 8px; }
  .contact p { font-size: 8px; line-height: 11px; color: var(--ink); white-space: nowrap; }
  .contact .label { color: var(--brand-red); }
  .contact .gap { margin-top: 4px; }
</style>
</head>
<body>

  <section class="letterhead" aria-label="Letterhead">
    <div class="wordmark"><span class="mark-square"></span>Juniper Anvil</div>
    <div class="blush-block"></div>
    <div class="fog-block"></div>
    <div class="footer-band">
      <p class="registration">Juniper Anvil is a Ltd Company registered in England &amp; Wales, Registration No. 05829147.</p>
    </div>
  </section>

  <section class="card card-front" aria-label="Business card front">
    <div class="blush-block"></div>
    <div class="wordmark"><span class="mark-square"></span>Juniper Anvil</div>
  </section>

  <section class="card card-back" aria-label="Business card back">
    <div class="wordmark"><span class="mark-square"></span>Juniper Anvil</div>
    <div class="blush-block"></div>
    <div class="fog-block"></div>
    <div class="contact">
      <div class="name">Marcus Telby</div>
      <div class="role">Web Developer</div>
      <p><span class="label">Address:</span> Suite 20938, 3rd Floor</p>
      <p>212-224 Orchard Lane, London, N7 9QX</p>
      <p class="gap"><span class="label">Phone:</span> 01632 960 418</p>
      <p><span class="label">Email:</span> marcus@juniperanvil.example</p>
      <p><span class="label">Web:</span> www.juniperanvil.example</p>
    </div>
  </section>

</body>
</html>
```